Business Card for a Jewellery Brand

Business card for an upscale jewellery brand. Attached is the brand logo and icon and color board. I am looking for two card versions: one for the founder and one is generic. The card should be elegant and convey upscale and premium feel. I am open to both square and rectangle card shapes.

Industry/Entity Type

Jewelry

Contact Information for Business Card

Two cards: (1) Sunila Perumbadi (Founder) (2) General
(1) Sunila Perumbadi card should have Name: Sunila Perumbadi, Title: Founder Email id: sunila@quelm.com.au. Phone no: +61412555307
(2) Generic card should have Email id: info@quelm.com.au. Phone no: +61431555962

Requirements
Must have
• Workmark
• ICON
• Phone no
• Email ID
• ABN: 48917205563 (Note: ABN is Business number in Australia)
• Website: www.quelm.com.au
• Instagram: quelm_jewellery
• Facebook: @quelmjewellery
Nice to have
• Tagline

```html
<!DOCTYPE html>
<html lang="en">
<head>
<meta charset="utf-8">
<title>QUELM Business Cards</title>
<link href="https://fonts.googleapis.com/css2?family=Great+Vibes&family=Mulish:wght@400;600&display=swap" rel="stylesheet">
<style>
  :root {
    --rose: #e0979a;
    --rose-line: #e7a7aa;
    --blush-light: #fdf6f4;
    --blush-mid: #f8e1dc;
    --ink: #141414;
    --card-edge: #d4d4d4;
    --page: #ffffff;
  }
  * { margin: 0; padding: 0; box-sizing: border-box; }
  html, body { width: 1200px; height: 1200px; overflow: hidden; background: var(--page); }
  .sheet { position: relative; width: 1200px; height: 1200px; }

  .card {
    position: absolute;
    width: 497px; height: 277px;
    border: 1px solid var(--card-edge);
    background: var(--page);
    font-family: "Mulish", Arial, sans-serif;
    color: var(--ink);
    overflow: hidden;
  }
  .card--front-top { left: 71px; top: 241px; }
  .card--back-top { left: 632px; top: 241px; }
  .card--front-bottom { left: 71px; top: 682px; }
  .card--back-bottom { left: 632px; top: 682px; }

  .marble-field {
    position: absolute; inset: 0;
    background: linear-gradient(135deg, var(--blush-light) 0%, var(--blush-mid) 30%, var(--blush-light) 50%, var(--blush-mid) 75%, var(--blush-light) 100%);
  }
  .inner-frame {
    position: absolute; left: 16px; top: 17px; right: 16px; bottom: 17px;
    border: 1.5px solid var(--rose-line);
  }
  .wordmark {
    position: absolute; left: 0; right: 0; top: 82px;
    text-align: center;
    font-family: "Mulish", Arial, sans-serif;
    font-weight: 600;
    font-size: 58px;
    letter-spacing: 0.22em;
    padding-left: 0.22em;
    color: var(--rose);
    line-height: 1;
  }
  .tagline-row {
    position: absolute; left: 87px; right: 87px; top: 204px;
    display: flex; align-items: center; gap: 12px;
  }
  .tagline-rule { flex: 1; height: 1px; background: var(--rose-line); }
  .tagline {
    font-family: "Great Vibes", cursive;
    font-size: 24px;
    color: var(--rose);
    white-space: nowrap;
  }

  .person-name {
    position: absolute; left: 0; right: 0; top: 46px;
    text-align: center;
    font-family: "Great Vibes", cursive;
    font-size: 48px;
    color: var(--rose);
    line-height: 1;
  }
  .person-title {
    position: absolute; right: 81px; top: 97px;
    font-size: 14px;
    color: var(--rose);
    letter-spacing: 0.01em;
  }
  .contact {
    position: absolute; left: 0; right: 0;
    text-align: center;
    white-space: nowrap;
  }
  .contact--founder { top: 150px; font-size: 15.5px; }
  .contact--founder .contact-line + .contact-line { margin-top: 4px; }
  .contact--general { top: 93px; font-size: 19.5px; }
  .contact--general .contact-line + .contact-line { margin-top: 5px; }
  .contact-line { line-height: 1.15; }
  .contact-line--primary { color: var(--ink); }
  .social { display: inline-flex; align-items: center; gap: 5px; }
  .social + .social { margin-left: 10px; }
  .social-dot { display: inline-block; border-radius: 50%; background: var(--rose); }
  .contact--founder .social-dot { width: 15px; height: 15px; }
  .contact--general .social-dot { width: 19px; height: 19px; }
</style>
</head>
<body>
<main class="sheet">

  <section class="card card--front-top" aria-label="Card front">
    <div class="marble-field" role="img" aria-label="Soft blush pink marble texture"></div>
    <div class="inner-frame"></div>
    <div class="wordmark">QUELM</div>
    <div class="tagline-row">
      <span class="tagline-rule"></span>
      <span class="tagline">Exquisite Silver Jewellery</span>
      <span class="tagline-rule"></span>
    </div>
  </section>

  <section class="card card--back-top" aria-label="Founder card back">
    <h1 class="person-name">Sunila Perumbadi</h1>
    <div class="person-title">FOUNDER</div>
    <div class="contact contact--founder">
      <p class="contact-line contact-line--primary">+6141 255 5307 | ABN: 4891 720 5563</p>
      <p class="contact-line">sunila@quelm.com.au. | www.quelm.com.au</p>
      <p class="contact-line">
        <span class="social"><span class="social-dot"></span>@quelmjewellery</span>
        <span class="social"><span class="social-dot"></span>quelm_jewellery</span>
      </p>
    </div>
  </section>

  <section class="card card--front-bottom" aria-label="Card front">
    <div class="marble-field" role="img" aria-label="Soft blush pink marble texture"></div>
    <div class="inner-frame"></div>
    <div class="wordmark">QUELM</div>
    <div class="tagline-row">
      <span class="tagline-rule"></span>
      <span class="tagline">Exquisite Silver Jewellery</span>
      <span class="tagline-rule"></span>
    </div>
  </section>

  <section class="card card--back-bottom" aria-label="General card back">
    <div class="contact contact--general">
      <p class="contact-line contact-line--primary">+6143 155 5962 | ABN: 4891 720 5563</p>
      <p class="contact-line">info@quelm.com.au. | www.quelm.com.au</p>
      <p class="contact-line">
        <span class="social"><span class="social-dot"></span>@quelmjewellery</span>
        <span class="social"><span class="social-dot"></span>quelm_jewellery</span>
      </p>
    </div>
  </section>

</main>
</body>
</html>
```